Christmas Post Card Mailing

We are a shipping Store. We will send RCTW don't need space for address. This is going to be our xmas mailing. We want a coupon on the Front that is 15% off when you spend over $20.00 (excludes qlbt) expires 12/31/14. Second offer get a free hat/scarf/gloves set when you spend over $50.00. First 100 customers. Not to be combined. I want it to look like xmas shipping, We also on the back want to have the Holiday shipping schedule. For East Coast and international shipping deadline is Dec 10th. For Mid west/west Coast deadline is Dec 16th. You can word it how it makes since and looks best. We have not received much response in the past for our postcards we really need something to jump out at them and wow them. We want that old fashion/western railroad look. Also on the back an open house on Dec.6th 3 prize give a ways.
KAR/ZTV/Movra/QLBT use logos
We also do: Mailbox Rental/ Faxing/copies/Notary/passport photos/Lamination/Shredding/Wine& Beer Shipping
We also sell: Phone accessories/shipping supplies/Office Supplies/Candles/Greeting cards/gift items

Update: we will use the large Post Card size.

Lantern Hollow Parcel
5873 Wexbury Dr.
Santa Rosa, Ca 95405
ph:707-555-0184
close to Calloway and Hwy47.
websites: www.lanternhollowparcel.com/www.sendfromwexbury.com
which ever website is best to list.

Target Market(s)

People who will need shipping for the Holidays.

Industry/Entity Type

Shipping

Other font styles liked:
• Western font

Requirements
Nice to have
• Maybe colors of xmas background of a postal courier pulling a sleigh full of presents? Or whatever looks best. Also thinking of having a xmas open house on dec 6th. Need picture on the front so people know what we do "shipping". Offers on the front/schedule and open house on the back. I like photos and full use of space No white with small fonts or marketing look. More movie trailer look. "Vintage" Artsy.Use our store photo on back to describe our open house.
Should not have
• No cartoons!! or animated pics. no white background.

```html
<!DOCTYPE html>
<html lang="en">
<head>
<meta charset="utf-8">
<title>Lantern Hollow Parcel – Holiday Postcard Back</title>
<link href="https://fonts.googleapis.com/css2?family=Archivo+Black&family=Arimo:ital,wght@0,400;0,700;1,700&family=Rye&display=swap" rel="stylesheet">
<style>
  :root {
    --page: #ffffff;
    --card: #ececec;
    --card-light: #f7f7f7;
    --red: #c5191f;
    --red-text: #c8202a;
    --ink: #1a1a1a;
    --white: #ffffff;
    --box-face: #e4e4e4;
    --box-edge: #9a9a9a;
  }
  * { margin: 0; padding: 0; box-sizing: border-box; }
  html, body { width: 1200px; height: 1000px; overflow: hidden; background: var(--page); }
  body { position: relative; font-family: "Arimo", Arial, sans-serif; color: var(--ink); }

  .postcard {
    position: absolute; left: 135px; top: 126px; width: 935px; height: 724px;
    background: var(--card);
    box-shadow: 0 18px 40px rgba(0,0,0,.35);
    overflow: hidden;
  }
  .message-side {
    position: absolute; left: 0; top: 0; width: 470px; height: 724px;
    background: radial-gradient(ellipse at 45% 45%, var(--card-light) 0%, var(--card) 75%);
  }

  .schedule-band {
    position: absolute; left: 0; top: 0; width: 702px; height: 92px;
    background: var(--red); border-bottom-right-radius: 8px; color: var(--white);
  }
  .schedule-title {
    position: absolute; left: 24px; top: 18px; font-family: "Archivo Black", Arial, sans-serif;
    font-size: 38px; letter-spacing: 2px; line-height: 1;
  }
  .schedule-subtitle {
    position: absolute; left: 24px; top: 57px; font-family: "Archivo Black", Arial, sans-serif;
    font-size: 16.5px; letter-spacing: 1px; line-height: 1;
  }
  .schedule-dates { position: absolute; left: 237px; top: 18px; font-size: 20.5px; line-height: 30px; white-space: nowrap; }
  .schedule-dates em { font-style: italic; font-weight: 700; }

  .carrier-stack { position: absolute; left: 10px; top: 100px; width: 110px; height: 130px; }
  .carrier-box {
    position: absolute; left: 0; width: 110px; height: 30px; background: var(--box-face);
    border: 1px solid var(--box-edge); border-radius: 3px;
    font-weight: 700; font-size: 18px; color: #333;
    display: flex; align-items: center; justify-content: center;
  }

  .services { position: absolute; left: 137px; top: 101px; font-size: 15px; line-height: 17.5px; white-space: nowrap; z-index: 2; }
  .services p + p { margin-top: 12px; }
  .services .label { color: var(--red-text); }

  .services-rule { position: absolute; left: 0; top: 231px; width: 313px; height: 2px; background: var(--red); }

  .delivery-photo {
    position: absolute; left: 482px; top: 92px; width: 220px; height: 139px;
    background: linear-gradient(160deg, #d9dadc 0%, #b9b3aa 45%, #8d7a62 75%, #2b2b2b 100%);
  }

  .open-house-title {
    position: absolute; left: 27px; top: 254px; font-family: "Rye", Georgia, serif;
    font-size: 40px; color: var(--red); line-height: 1; white-space: nowrap;
  }
  .store-mark { position: absolute; left: 335px; top: 248px; display: flex; align-items: center; gap: 6px; }
  .store-mark .dot { width: 18px; height: 18px; border-radius: 50%; background: var(--ink); }
  .store-mark .name { font-size: 13px; font-weight: 700; width: 90px; line-height: 15px; }

  .open-house-date { position: absolute; left: 153px; top: 305px; font-size: 20px; }
  .open-house-prizes { position: absolute; left: 205px; top: 333px; font-size: 20px; color: var(--red-text); }

  .gift-image {
    position: absolute; left: 15px; top: 365px; width: 405px; height: 215px;
    background: radial-gradient(ellipse at 45% 55%, #c8232b 0%, #b01a22 45%, rgba(176,26,34,0) 72%);
  }

  .area-label { position: absolute; font-size: 26px; text-align: center; line-height: 33px; }
  .postage-label { left: 743px; top: 95px; width: 130px; }
  .address-label { left: 584px; top: 284px; width: 200px; }
  .barcode-label { left: 424px; top: 637px; width: 200px; }
  .address-note { position: absolute; left: 500px; top: 363px; font-size: 18.5px; line-height: 24px; white-space: nowrap; }
</style>
</head>
<body>
  <main class="postcard">
    <section class="message-side"></section>

    <header class="schedule-band">
      <h1 class="schedule-title">HOLIDAY</h1>
      <p class="schedule-subtitle">shipping schedule</p>
      <p class="schedule-dates">East Coast and international deadline is <em>Dec 10th</em><br>Mid west/west Coast deadline is <em>Dec 16th</em></p>
    </header>

    <div class="delivery-photo" role="img" aria-label="Photo of a delivery truck, cargo plane, parcels and a courier"></div>

    <div class="carrier-stack" aria-label="Carriers we ship with">
      <div class="carrier-box" style="top:0">KAR</div>
      <div class="carrier-box" style="top:33px">ZTV</div>
      <div class="carrier-box" style="top:66px">Movra</div>
      <div class="carrier-box" style="top:99px">QLBT</div>
    </div>

    <div class="services">
      <p><span class="label">We also do:</span> Mailbox Rental/ Faxing/copies<br>Notary/passport photos/Lamination/Shredding<br>Wine&amp; Beer Shipping</p>
      <p><span class="label">We also sell:</span> Phone accessories/shipping<br>supplies/Office Supplies/Candles/Greeting<br>cards/gift items</p>
    </div>
    <div class="services-rule"></div>

    <div class="gift-image" role="img" aria-label="Photo of red wrapped Christmas presents with gold bows, a Santa hat and ornaments"></div>

    <h2 class="open-house-title">OPEN HOUSE</h2>
    <div class="store-mark"><span class="dot"></span><span class="name">Lantern Hollow Parcel</span></div>
    <p class="open-house-date">on December 6th</p>
    <p class="open-house-prizes">3 prize give a ways</p>

    <p class="area-label postage-label">Postage<br>Area</p>
    <p class="area-label address-label">Address Area</p>
    <p class="address-note">The only text allowed in the Address Area<br>is the recipient mailing address.<br>Red zones may have no text or<br>graphics darker than 7% grayscale.</p>
    <p class="area-label barcode-label">Barcode Area</p>
  </main>
</body>
</html>
```